Need designers to make a boring check list funky and fun

We are an executive rental company based in Sydney. We deal in fully furnished properties for both short and long term bookings. We have a check list for home owners to help them prepare their home for guests.
We are looking for an interesting design which makes the mundane tasks seem both fun and enjoyable.
Target Market(s)
single, couples and families where they are dual income households. Highly educated, high powered jobs with little to no time and are stressed needing a break, but also needing to pay the mortgage.
Industry/Entity Type
It Company
Colors
Designer to choose colors to be used in the design.
Requirements
Must have
- images of house rooms, clean.
- our logo on it
Nice to have
- icons for each section ie person swimming for a pool
Should not have
- just text no images

```html
<!DOCTYPE html>
<html lang="en">
<head>
<meta charset="utf-8">
<title>Harbourline Stays – Home Preparation Checklist</title>
<link href="https://fonts.googleapis.com/css2?family=Barlow:wght@400;500;600&family=Barlow+Semi+Condensed:wght@500;600&display=swap" rel="stylesheet">
<style>
  :root{
    --magenta:#e0157c;
    --magenta-dark:#c20f68;
    --band:#d5d6d8;
    --paper:#f7f7f7;
    --ink:#3b3b3d;
    --ink-soft:#6a6a6d;
    --backdrop:#c8cbcb;
  }
  *{box-sizing:border-box;margin:0;padding:0}
  html,body{width:1200px;height:800px;overflow:hidden}
  body{background:var(--backdrop);font-family:"Barlow",Arial,sans-serif;color:var(--ink)}
  .canvas{display:grid;grid-template-columns:600px 600px;grid-template-rows:400px 400px;width:1200px;height:800px}
  .cell{position:relative}
  .spread{position:absolute;left:25px;top:28px;width:550px;height:344px;display:flex;box-shadow:0 6px 18px rgba(0,0,0,.18)}
  .page{position:relative;width:275px;height:344px;background:var(--paper);overflow:hidden}
  .page--left{box-shadow:inset -8px 0 10px -8px rgba(0,0,0,.18)}
  .page--right{box-shadow:inset 8px 0 10px -8px rgba(0,0,0,.14)}

  .band{position:absolute;top:18px;height:7px;background:var(--band)}
  .band--left{left:0;right:0}
  .band--right{left:0;right:0}
  .tab{position:absolute;top:16px;left:0;width:14px;height:11px;background:var(--magenta)}

  .photo{position:absolute;display:block}
  .photo--house{background:linear-gradient(180deg,#e4e4e4 0%,#bdbdbd 45%,#8d8d8d 70%,#cfcfcf 100%)}
  .photo--resort{background:linear-gradient(180deg,#55678c 0%,#3a4968 45%,#2b2f3e 70%,#1b2233 100%)}
  .photo--lounge{background:linear-gradient(180deg,#8b8b8b 0%,#bcbcbc 55%,#e8e8e8 100%)}
  .photo--kitchen{background:linear-gradient(160deg,#dcdcdc 0%,#9a9a9a 50%,#3c3c3c 100%)}
  .photo--bedroom{background:linear-gradient(180deg,#bfbfbf 0%,#7c7c7c 55%,#d6d6d6 100%)}
  .photo--laundry{background:linear-gradient(180deg,#6d6d6d,#2d2d2d)}
  .photo--pool{background:linear-gradient(180deg,#9fb7a8 0%,#7f9a8e 45%,#6fa8a8 70%,#4b8e96 100%)}

  .frame{position:absolute;right:-2px;width:34px;height:38px;border:2px solid var(--magenta);border-right:none;border-radius:5px 0 0 5px}
  .frame::before,.frame::after{content:"";position:absolute;right:-40px;width:46px;height:2px;background:var(--magenta)}
  .frame::before{top:-2px}.frame::after{bottom:-2px}

  .heading{font-family:"Barlow Semi Condensed",Arial,sans-serif;font-weight:600;font-size:9px;letter-spacing:.9px;text-transform:uppercase;color:var(--ink);position:relative;padding-bottom:3px;margin-bottom:4px}
  .heading::after{content:"";position:absolute;left:0;bottom:0;width:16px;height:1.5px;background:var(--magenta)}
  .checklist{list-style:none}
  .checklist li{position:relative;font-size:5.4px;line-height:1.38;padding-left:8px;margin-bottom:2.2px;color:var(--ink-soft)}
  .checklist li::before{content:"";position:absolute;left:1px;top:1.4px;width:2.2px;height:3.8px;border:solid var(--magenta);border-width:0 1px 1px 0;transform:rotate(45deg)}
  .section{position:absolute}
  .boxed{border:1px solid var(--magenta);padding:5px 6px}

  /* cover */
  .back-cover{background:linear-gradient(135deg,var(--magenta) 0%,var(--magenta-dark) 100%)}
  .back-cover .stripe{position:absolute;left:22px;top:24px;width:10px;height:108px;background:#fff}
  .final-bits{position:absolute;left:24px;top:188px;width:200px;color:#fff}
  .final-bits h2{font-family:"Barlow Semi Condensed",Arial,sans-serif;font-size:8.5px;font-weight:600;letter-spacing:.4px;margin-bottom:6px}
  .final-bits p{font-size:5.6px;line-height:1.4;margin-bottom:5px;opacity:.95}
  .front-cover .stripe{position:absolute;right:26px;top:0;width:9px;height:56px;background:var(--magenta)}
  .front-cover .stripe::after{content:"";position:absolute;left:3px;top:0;width:3px;height:44px;background:#fff}
  .brand-block{position:absolute;left:58px;top:200px;width:118px;height:86px;background:var(--magenta);display:flex;flex-direction:column;align-items:center;justify-content:center;gap:7px}
  .brand-mark{width:14px;height:14px;background:#fff}
  .brand-name{font-family:"Barlow",Arial,sans-serif;font-weight:500;font-size:7px;letter-spacing:1.6px;text-transform:uppercase;color:#fff}
</style>
</head>
<body>
<main class="canvas">

  <!-- Cover -->
  <section class="cell">
    <div class="spread">
      <div class="page page--left back-cover">
        <span class="stripe"></span>
        <div class="final-bits">
          <h2>YOUR ALMOST THERE… FINAL BITS</h2>
          <p>Provide a set of keys for Harbourline Stays</p>
          <p>Arrange rubbish to be placed out on street when required, we can arrange this at a fee</p>
          <p>Let us know of any areas which could be affected by heavy rain</p>
          <p>Cleaners come in to set up the property prior to guests arrival</p>
        </div>
      </div>
      <div class="page page--right front-cover">
        <span class="photo photo--house" role="img" aria-label="Black and white photo of a two storey brick family home with front lawn" style="left:0;top:64px;width:275px;height:190px"></span>
        <span class="stripe"></span>
        <div class="brand-block">
          <span class="brand-mark"></span>
          <span class="brand-name">Harbourline Stays</span>
        </div>
      </div>
    </div>
  </section>

  <!-- General / Living room -->
  <section class="cell">
    <div class="spread">
      <div class="page page--left">
        <span class="band band--left"></span><span class="tab"></span>
        <div class="section" style="left:24px;top:46px;width:230px">
          <h3 class="heading">General</h3>
          <ul class="checklist">
            <li>Provide spare light bulbs and batteries for all remotes</li>
            <li>Put felt pads under furniture to protect the floors</li>
            <li>Put coasters under any furniture with wheels</li>
            <li>Remove any personal items such as photos</li>
            <li>Lock away all linen including tea towels</li>
            <li>Unplug any home phones</li>
            <li>Leave router in an area easy to reach by guests</li>
            <li>Network name and password to be provided</li>
            <li>Property to be pest sprayed for cockroaches and ants</li>
          </ul>
        </div>
        <span class="photo photo--resort" role="img" aria-label="Photo of a resort pool with palm trees at dusk" style="left:24px;top:178px;width:228px;height:140px"></span>
      </div>
      <div class="page page--right">
        <span class="band band--right"></span>
        <span class="photo photo--lounge" role="img" aria-label="Black and white photo of a living room with a long sofa and framed pictures" style="left:20px;top:30px;width:255px;height:118px"></span>
        <span class="frame" style="top:34px"></span>
        <div class="section" style="left:22px;top:168px;width:236px">
          <h3 class="heading">Living room</h3>
          <ul class="checklist">
            <li>Check all furniture, rugs and floors have no rips, tears or stains</li>
            <li>Wash or steam clean cushion covers</li>
            <li>Steam clean any upholstery if it requires it</li>
            <li>Purchase an annual carpet, upholstery and rugs clean</li>
            <li>Put in new batteries for remotes and smoke alarms</li>
            <li>Leave instructions on how to work all electronics</li>
            <li>Set up a guest password for streaming apps</li>
          </ul>
        </div>
      </div>
    </div>
  </section>

  <!-- Kitchen / Laundry / Bedrooms / Bathrooms / Stairs -->
  <section class="cell">
    <div class="spread">
      <div class="page page--left">
        <span class="band band--left"></span><span class="tab"></span>
        <span class="photo photo--kitchen" role="img" aria-label="Black and white photo of a modern kitchen with island bench" style="left:0;top:36px;width:128px;height:210px"></span>
        <div class="section" style="left:138px;top:36px;width:124px">
          <h3 class="heading">Kitchen</h3>
          <ul class="checklist">
            <li>Empty pantry, fridge and freezer</li>
            <li>Thoroughly clean oven and microwave</li>
            <li>Wipe out cupboards and drawers</li>
            <li>Clean out fridge and freezer</li>
            <li>Check all appliances are working</li>
            <li>Run dishwasher with a cleaner</li>
            <li>Remove any expired food items</li>
            <li>Check crockery is not chipped</li>
            <li>Leave crockery for all guests</li>
          </ul>
        </div>
        <div class="section boxed" style="left:18px;top:258px;width:240px">
          <h3 class="heading">Laundry</h3>
          <ul class="checklist">
            <li>Clean out lint filter from the dryer</li>
            <li>Ensure there is a drying rack and an ironing board</li>
            <li>Leave instructions on how to operate the washing machine</li>
          </ul>
        </div>
        <span class="photo photo--laundry" role="img" aria-label="Photo of clothes hanging on a rail" style="left:200px;top:246px;width:60px;height:22px"></span>
      </div>
      <div class="page page--right">
        <span class="band band--right"></span>
        <span class="photo photo--bedroom" role="img" aria-label="Black and white photo of a neatly made bedroom" style="left:14px;top:30px;width:180px;height:58px"></span>
        <span class="frame" style="top:34px"></span>
        <div class="section" style="left:20px;top:100px;width:238px">
          <h3 class="heading">Bedrooms</h3>
          <ul class="checklist">
            <li>Clear the robes for guests to use in each of the bedrooms</li>
            <li>Check all mattress protectors and pillow protectors are clean</li>
            <li>Supply spare blankets and pillows for all sofa beds</li>
          </ul>
          <h3 class="heading" style="margin-top:6px">Bathrooms</h3>
          <ul class="checklist">
            <li>Ensure all mould is removed from the shower</li>
            <li>Check all grout and silicone is in good order</li>
            <li>Make sure exhaust fans are working and clean</li>
            <li>Clear out all cabinets including all medicines</li>
            <li>Leave a new hair dryer for guests</li>
          </ul>
        </div>
        <div class="section boxed" style="left:20px;top:278px;width:238px;display:flex;gap:12px;align-items:flex-start">
          <h3 class="heading">Stairs</h3>
          <ul class="checklist">
            <li>Check the balustrade and railings are secure</li>
            <li>Repair any loose carpet</li>
          </ul>
        </div>
      </div>
    </div>
  </section>

  <!-- Outside / Safety / Pool / Insurance -->
  <section class="cell">
    <div class="spread">
      <div class="page page--left">
        <span class="band band--left"></span><span class="tab"></span>
        <span class="photo photo--pool" role="img" aria-label="Photo of a resort swimming pool with palm trees" style="left:150px;top:36px;width:125px;height:160px"></span>
        <div class="section" style="left:22px;top:40px;width:124px">
          <h3 class="heading">Outside</h3>
          <ul class="checklist">
            <li>Ensure all balconies and railings are stable and safe</li>
            <li>Check height of balcony railings is compliant</li>
            <li>Get gardener to cut back any branches</li>
            <li>Arrange gardener to maintain garden regularly</li>
            <li>Ensure automatic watering is working</li>
            <li>Clean BBQ and outdoor furniture</li>
            <li>Jet blast mould from outdoor surfaces</li>
            <li>Remove cobwebs and clean gutters</li>
            <li>Ensure outdoor lighting is operational</li>
            <li>Windows to be cleaned and sparkling</li>
          </ul>
        </div>
        <div class="section boxed" style="left:156px;top:206px;width:100px">
          <h3 class="heading">Safety</h3>
          <ul class="checklist">
            <li>Provide fire extinguisher and blanket</li>
            <li>Repair broken tiles and steps</li>
            <li>Patch any holes in walls</li>
            <li>Check smoke alarms working</li>
          </ul>
        </div>
      </div>
      <div class="page page--right">
        <span class="band band--right"></span>
        <span class="photo photo--pool" role="img" aria-label="Photo of a resort swimming pool with palm trees and white buildings" style="left:0;top:36px;width:250px;height:160px"></span>
        <span class="frame" style="top:44px"></span>
        <div class="section boxed" style="left:18px;top:212px;width:96px">
          <h3 class="heading">Pool</h3>
          <ul class="checklist">
            <li>Pool and fencing to be fully compliant</li>
            <li>Arrange regular pool cleaning service</li>
            <li>Leave instructions for the pool equipment</li>
          </ul>
        </div>
        <div class="section" style="left:126px;top:206px;width:132px">
          <h3 class="heading">Insurance</h3>
          <ul class="checklist">
            <li>Get landlord and tenants insurance</li>
            <li>Take photos of contents and of your home</li>
            <li>Lock away any valuables</li>
          </ul>
        </div>
      </div>
    </div>
  </section>

</main>
</body>
</html>
```